UNABLE TO FIND SUITABLE ICT TALENT IN NEW ZEALAND? WE CAN HELP.

We need a brochure to sell our migration services to ICT (Information and Communication Technologies) recruiters in New Zealand. We are a New Zealand based migration company headed by a Licensed Immigration Adviser and we can bring in specific talents into New Zealand. We are aware ICT is in the long term skill shortage area and that recruiters and companies are struggling to find the right ICT talent. So over the past two years we have developed a high quality global ICT talent pool who are keen to work in New Zealand. And we have the expertise to and process their legal entry into New Zealand bring them in at short notice. We need a brochure that conveys a strong New Zealand connect, confidence and trust.

Target Market(s)

New Zealand ICT Recruiters and Companies who need ICT talent

Industry/Entity Type

Communication

Contact Information for Business Card

Corwin Haltey
Senior Manager - Operations
Mobile: 0274318296

Font styles to use
Serif

Requirements
Must have
• A strong ICT and New Zealand theme. Must have the following Maori proverb on the rear with the English translation. The rear side of the card which has this proverb must also have a strong Maori theme.
• Naku te rourou nau te rourou ka ora ai te iwi - With your basket and my basket the people will live
Nice to have
• The brochure/flyer is intended to be an A4 size folded in half, so that we can print and mail it to our target clients. Remember this is an A4 flyer folded in the middle. So it has got cover + back + 2 inside pages in all.

```html
<!DOCTYPE html>
<html lang="en">
<head>
<meta charset="utf-8">
<title>RMK Group – Think New Zealand brochure</title>
<link rel="stylesheet" href="https://fonts.googleapis.com/css2?family=Lato:wght@400;700&family=Tinos:wght@400;700&display=swap">
<style>
  :root{
    --bg:#ece9e4;
    --ink:#111111;
    --purple:#7d1289;
    --purple-deep:#5a0a66;
    --pink:#e0457b;
    --grey:#bdbdbd;
    --white:#ffffff;
    --text:#1c1c1c;
  }
  *{box-sizing:border-box;margin:0;padding:0}
  html,body{width:1200px;height:900px;overflow:hidden;background:var(--bg)}
  .canvas{position:relative;width:1200px;height:900px}
  .page{position:absolute;top:65px;width:540px;height:770px;overflow:hidden;background:var(--white)}
  .page--back{left:60px}
  .page--cover{left:600px}

  /* back page */
  .back-dark{position:absolute;left:0;top:0;width:540px;height:600px;
    background:linear-gradient(180deg,#222 0%,#0e0e0e 55%,#2a2a2a 100%)}
  .city-texture{position:absolute;left:0;top:190px;width:540px;height:380px;
    background:radial-gradient(ellipse at 50% 55%,rgba(90,90,90,.45),rgba(20,20,20,0) 70%)}
  .proverb{position:absolute;left:45px;top:83px;width:455px;height:119px;
    background:linear-gradient(120deg,#8e2a9b 0%,var(--purple) 45%,#6c1279 100%);color:var(--white)}
  .proverb__title{font-family:"Tinos",serif;font-weight:400;font-size:24px;text-align:center;margin-top:10px;line-height:1}
  .proverb__rule{width:60px;height:2px;background:var(--pink);margin:7px auto 0}
  .proverb__cols{position:relative;font-family:"Lato",sans-serif;font-size:17px;line-height:18px}
  .proverb__cols p{position:absolute;top:12px}
  .proverb__maori{left:17px;width:190px}
  .proverb__english{left:254px;width:186px}
  .about{position:absolute;left:50px;top:318px;width:440px;color:var(--white);
    font-family:"Lato",sans-serif;font-size:16px;line-height:18.5px;letter-spacing:.6px;
    text-align:justify;text-align-last:center;hyphens:auto;-webkit-hyphens:auto}
  .swoosh{position:absolute;left:0;width:540px}
  .back-footer{position:absolute;left:0;top:598px;width:540px;height:172px;background:var(--white)}
  .contact{position:absolute;left:38px;top:22px;font-family:"Lato",sans-serif;font-size:16px;color:var(--text);line-height:17px}
  .contact__row{display:flex;align-items:flex-start;gap:8px;margin-bottom:9px}
  .contact__row svg{flex:none;margin-top:1px}
  .brand{position:absolute;display:flex;align-items:center;gap:8px;
    font-family:"Tinos",serif;font-weight:700;color:var(--ink);letter-spacing:1px}
  .brand__dot{border-radius:50%;background:var(--ink)}
  .back-footer .brand{left:370px;top:58px;font-size:44px}
  .back-footer .brand__dot{width:16px;height:16px}

  /* cover page */
  .cover-top{position:absolute;left:0;top:0;width:540px;height:185px;
    background:linear-gradient(135deg,#3a3a3a 0%,#111 40%,#2b2b2b 70%,#0c0c0c 100%)}
  .ribbon{position:absolute;left:38px;top:0;width:136px;height:178px}
  .ribbon .brand{left:18px;top:50px;font-size:36px}
  .ribbon .brand__dot{width:12px;height:12px}
  .skyline{position:absolute;left:0;top:180px;width:540px;height:400px;
    background:linear-gradient(180deg,#9a9a9a 0%,#d8d8d8 30%,#bcbcbc 55%,#5b5b5b 75%,#3c3c3c 100%)}
  .cover-footer{position:absolute;left:0;top:598px;width:540px;height:172px;background:var(--white);text-align:center}
  .cover-footer__think{font-family:"Lato",sans-serif;font-size:22px;color:var(--ink);margin-top:12px;line-height:1}
  .cover-footer__title{font-family:"Tinos",serif;font-weight:700;font-size:37px;color:var(--purple);line-height:1;margin-top:2px;letter-spacing:.5px}
  .cover-footer__tag{font-family:"Lato",sans-serif;font-size:17px;color:var(--ink);line-height:19px;margin-top:2px}
  .cover-footer__url{display:inline-block;margin-top:12px;width:280px;height:24px;border-radius:12px;
    background:var(--purple);color:var(--white);font-family:"Tinos",serif;font-size:16px;line-height:24px}
  .fold{position:absolute;left:598px;top:65px;width:4px;height:770px;
    background:linear-gradient(90deg,rgba(0,0,0,.25),rgba(0,0,0,0))}
</style>
</head>
<body>
<main class="canvas">

  <section class="page page--back" aria-label="Back page">
    <div class="back-dark"></div>
    <div class="city-texture" role="img" aria-label="Dark photo of office towers seen from below"></div>

    <div class="proverb" role="group" aria-label="Maori proverb">
      <h2 class="proverb__title">Maori proverb</h2>
      <div class="proverb__rule"></div>
      <div class="proverb__cols">
        <p class="proverb__maori" lang="mi">Naku te rourou nau te rourou ka ora ai te iwi</p>
        <p class="proverb__english">With your basket and my basket the people will live</p>
      </div>
    </div>

    <p class="about">RMK group is a New Zealand based business house with current interests in migration and information technology. Success through simplicity is the credo that underpins all our products and services for the benefit of our customers, employees, shareholders and community.</p>

    <svg class="swoosh" style="top:500px" width="540" height="100" viewBox="0 0 540 100" aria-hidden="true">
      <path d="M0 15 C150 60 360 95 540 88 L540 100 L0 100Z" fill="var(--grey)"/>
      <path d="M0 48 C160 80 360 100 540 96 L540 100 L0 100Z" fill="var(--purple)"/>
      <path d="M0 78 C120 92 220 98 300 100 L0 100Z" fill="var(--purple-deep)"/>
    </svg>

    <div class="back-footer">
      <div class="contact">
        <div class="contact__row">
          <svg width="18" height="16" viewBox="0 0 18 16" aria-hidden="true"><path d="M9 1 L17 8 H14.5 V15 H10.5 V10.5 H7.5 V15 H3.5 V8 H1Z" fill="var(--purple)"/></svg>
          <span>RMK Migration Ltd, 54 Harbour<br>Lane, Riverside, Hamilton<br>3214</span>
        </div>
        <div class="contact__row">
          <svg width="18" height="14" viewBox="0 0 18 14" aria-hidden="true"><rect x="1" y="2" width="16" height="11" fill="var(--purple)"/><path d="M1 2 L9 8 L17 2" stroke="#fff" stroke-width="1.4" fill="none"/></svg>
          <span>hello@rmk.kiwi</span>
        </div>
        <div class="contact__row">
          <svg width="18" height="18" viewBox="0 0 18 18" aria-hidden="true"><g fill="none" stroke="var(--purple)" stroke-width="1.4"><circle cx="9" cy="9" r="7.5"/><ellipse cx="9" cy="9" rx="3.3" ry="7.5"/><path d="M1.5 9H16.5M3 5H15M3 13H15"/></g></svg>
          <span>www.rmk.kiwi.com</span>
        </div>
      </div>
      <div class="brand"><span class="brand__dot"></span>RMK</div>
    </div>
  </section>

  <section class="page page--cover" aria-label="Front cover">
    <div class="cover-top" role="img" aria-label="Dark abstract photo of stacked black cubes"></div>
    <div class="skyline" role="img" aria-label="Black and white photo of a city skyline with a tall observation tower and harbour cranes"></div>

    <svg class="swoosh" style="top:40px" width="540" height="150" viewBox="0 0 540 150" aria-hidden="true">
      <path d="M0 140 C200 110 400 60 540 10 L540 28 C400 80 220 125 0 150Z" fill="var(--white)"/>
      <path d="M0 150 C220 128 400 95 540 55 L540 150Z" fill="var(--purple)"/>
    </svg>

    <div class="ribbon">
      <svg width="136" height="178" viewBox="0 0 136 178" aria-hidden="true">
        <path d="M0 0 H136 V178 L68 150 L0 178Z" fill="var(--white)"/>
      </svg>
      <div class="brand"><span class="brand__dot"></span>RMK</div>
    </div>

    <svg class="swoosh" style="top:500px" width="540" height="100" viewBox="0 0 540 100" aria-hidden="true">
      <path d="M0 80 C200 60 400 30 540 5 L540 100 L0 100Z" fill="var(--grey)"/>
      <path d="M0 92 C220 82 400 60 540 45 L540 100 L0 100Z" fill="var(--purple)"/>
      <path d="M0 90 H540 V100 H0Z" fill="var(--purple)"/>
    </svg>

    <div class="cover-footer">
      <p class="cover-footer__think">THINK</p>
      <h1 class="cover-footer__title">NEW ZEALAND</h1>
      <p class="cover-footer__tag">ONE AMAZING COUNTRY,<br>MANY AWESOME OPPORTUNITIES.</p>
      <span class="cover-footer__url">www.rmk.kiwi.com</span>
    </div>
  </section>

  <div class="fold" aria-hidden="true"></div>
</main>
</body>
</html>
```